This is a label for a new sake made in Japan imported into Aust

This will be a bottle label for a new sake imported into Australia. The hero of the label is the Velmora. We have joined the "O" meaning great in Japanese and used sake with "Z" to have Velmora with the play on words using Oz as in our slang for Aussie. A modern label with a Japanese take is key. This is a premium sake made in Japan for the Australian market.
The "Tall Casks" up the top is the name of the company, we have yet to design a logo for the company.

Target Market(s)

Alcohol

Logo Text

Velmora

Font styles to use
Serif

Requirements
Must have
• easy to read, with a hint of Japanese origin
Should not have
• too busy

```html
<!DOCTYPE html>
<html lang="en">
<head>
<meta charset="utf-8">
<title>Velmora Premium Japanese Sake Label</title>
<link rel="stylesheet" href="https://fonts.googleapis.com/css2?family=Architects+Daughter&family=Oswald:wght@700&family=Noto+Serif+JP:wght@400&display=swap">
<style>
  :root {
    --ink: #111111;
    --red: #ff0000;
    --ghost: #e4e4e4;
    --paper: #ffffff;
  }
  html, body {
    margin: 0;
    padding: 0;
    overflow: hidden;
    background: var(--paper);
  }
  .label {
    position: relative;
    width: 1000px;
    height: 1200px;
    overflow: hidden;
    background: var(--paper);
  }
  .company-bar {
    position: absolute;
    top: 8px;
    left: 0;
    width: 1000px;
    height: 62px;
  }
  .company-bar__pattern {
    position: absolute;
    top: 2px;
    width: 164px;
    height: 56px;
    background: linear-gradient(180deg, #ff4d4d, var(--red));
    opacity: 0.85;
  }
  .company-bar__pattern--left { left: 0; }
  .company-bar__pattern--right { right: 0; width: 178px; }
  .company-name {
    position: absolute;
    left: 190px;
    width: 610px;
    top: -6px;
    margin: 0;
    font-family: "Oswald", sans-serif;
    font-weight: 700;
    font-size: 58px;
    line-height: 70px;
    color: var(--ink);
    display: flex;
    justify-content: space-between;
  }
  .blossom {
    position: absolute;
    left: 304px;
    top: 254px;
    width: 392px;
    height: 194px;
    border-radius: 50% 50% 0 0;
    background: radial-gradient(ellipse at 50% 100%, #ffd6d6 0%, var(--red) 100%);
    opacity: 0.9;
  }
  .rule {
    position: absolute;
    left: 57px;
    width: 891px;
    height: 15px;
    background: var(--red);
  }
  .rule--top { top: 457px; }
  .rule--bottom { top: 748px; left: 54px; width: 890px; }
  .brand {
    position: absolute;
    left: 57px;
    top: 490px;
    width: 900px;
    height: 240px;
    display: flex;
    align-items: center;
    gap: 14px;
  }
  .brand__disc {
    flex: none;
    width: 226px;
    height: 212px;
    border-radius: 50%;
    background: var(--ink);
  }
  .brand__name {
    margin: 0;
    font-family: "Architects Daughter", cursive;
    font-weight: 400;
    font-size: 172px;
    line-height: 1;
    color: var(--ink);
  }
  .stem-mark {
    position: absolute;
    left: 430px;
    top: 769px;
    width: 155px;
    height: 74px;
    background: linear-gradient(180deg, var(--red), #ff9999);
    clip-path: polygon(0 10%, 100% 10%, 54% 45%, 52% 100%, 48% 100%, 46% 45%);
  }
  .kanji-backdrop {
    position: absolute;
    left: 0;
    top: 850px;
    width: 1000px;
    margin: 0;
    display: flex;
    justify-content: space-between;
    font-family: "Noto Serif JP", serif;
    font-size: 330px;
    line-height: 1;
    color: var(--ghost);
  }
  .descriptor {
    position: absolute;
    left: 0;
    top: 912px;
    width: 1000px;
    margin: 0;
    text-align: center;
    font-family: "Architects Daughter", cursive;
    font-size: 72px;
    line-height: 78px;
    color: var(--ink);
  }
</style>
</head>
<body>
<main class="label">
  <header class="company-bar">
    <div class="company-bar__pattern company-bar__pattern--left" role="img" aria-label="Red Japanese lattice pattern"></div>
    <h2 class="company-name" aria-label="Tall Casks">
      <span>T</span><span>A</span><span>L</span><span>L</span><span>C</span><span>A</span><span>S</span><span>K</span><span>S</span>
    </h2>
    <div class="company-bar__pattern company-bar__pattern--right" role="img" aria-label="Red Japanese lattice pattern"></div>
  </header>

  <div class="blossom" role="img" aria-label="Red cherry blossom ornament"></div>
  <div class="rule rule--top"></div>

  <section class="brand">
    <div class="brand__disc"></div>
    <h1 class="brand__name">Velmora</h1>
  </section>

  <div class="rule rule--bottom"></div>
  <div class="stem-mark" role="img" aria-label="Small red blossom stem ornament"></div>

  <p class="kanji-backdrop" aria-hidden="true"><span>日</span><span>本</span><span>酒</span></p>

  <p class="descriptor">PREMIUM<br>JAPANESE<br>SAKE</p>
</main>
</body>
</html>
```